Webdesign für SEO-Agentur
Zielgruppe
Wir bieten kleinen und mittelständischen Unternehmen Suchmaschinenoptimierung zum fairen Preis mit Erfolgsgarantie an. Unsere Zielgruppe sind Unternehmer die bisher wenig oder gar keine Erfahrungen mit SEO hatten. Wir möchten Unternehmen dabei helfen ihren digitalen Auftritt sowie dessen Sichtbarkeit zu verbessern um neue Kunden zu finden.
Aufgabenstellung
- seriöses und modernes Design bei gleichzeitig ansprechender Gestaltung
- passend zum Namen möchten wir, dass die Website einen leichten wissenschaftlichen/chemischen Touch erhält. Beachten Sie daher unsere Skizze zur Schritt für Schritt Darstellung. Weitere kleine Hinweise in Richtung Chemie oder Wissenschaft können und sollen eingebaut werden.
- vorerst nur Landing-Page, daher keine Navigation nötig. Wir erwarten eine vollständige Desktop sowie Mobilversion in Ihrem Design.
- Einhaltung der vorgegebenen Inhalte
- keine langweiligen Standard-Designs, auch besondere Seiten können seriös sein
- Header ist für Portrait der Mitarbeiter reserviert und benötigt daher eine gewisse freie Fläche

```html
<!DOCTYPE html>
<html lang="de">
<head>
<meta charset="utf-8">
<title>SEO Agentur – Abrechnung auf Erfolgsbasis</title>
<link href="https://fonts.googleapis.com/css2?family=Lato:wght@300;400;700;900&display=swap" rel="stylesheet">
<style>
:root{
  --navy:#0f3b68;
  --red:#e8174a;
  --text:#7a7a7f;
  --bg:#f4f4f6;
  --card:#ffffff;
  --white:#ffffff;
}
*{box-sizing:border-box;margin:0;padding:0}
html,body{width:1200px;height:4167px;overflow:hidden}
body{font-family:'Lato',sans-serif;color:var(--text);background:var(--white)}
.page{position:relative;width:1200px;height:4167px;background:var(--bg);overflow:hidden}
.page::before{content:"";position:absolute;left:0;top:0;width:40px;height:100%;background:var(--white);z-index:3}
.deco{position:absolute;z-index:1}
.abs{position:absolute;z-index:2}
h2{color:var(--navy);font-weight:700;text-align:center;line-height:1.25}
.center{text-align:center}
p{font-size:13px;line-height:21.5px;font-weight:300}
.btn{display:block;background:var(--red);color:var(--white);font-size:14px;font-weight:400;text-align:center;border-radius:22px;text-decoration:none;line-height:41px;height:41px}
.section-title{font-size:28px}
.side-title{color:var(--red);font-size:14px;font-weight:700;margin-bottom:24px}
.side p{font-size:12px;line-height:20px}
.photo{background:linear-gradient(135deg,#c9ccd2,#8d959f)}
.card{background:var(--card);box-shadow:0 1px 4px rgba(0,0,0,.05)}
.card .photo{height:193px}
.card h3{color:var(--red);font-size:14px;font-weight:700;margin:34px 25px 14px;line-height:18px}
.card p{font-size:12px;line-height:20px;margin:0 25px}
.feature h3{color:var(--red);font-size:14px;font-weight:700;margin:34px 25px 20px}
.benefit{position:absolute;display:flex;gap:20px;align-items:flex-start}
.benefit strong{display:block;color:#333;font-size:14px;font-weight:700;line-height:20px}
.benefit span{font-size:14px;font-weight:300;line-height:20px}
.tick{width:30px;height:30px;flex:none;margin-top:4px}
</style>
</head>
<body>
<main class="page">

  <svg class="deco" style="left:40px;top:0" width="200" height="530" viewBox="0 0 200 530" aria-hidden="true">
    <path d="M0 0 H110 Q230 40 180 130 L0 525 Z" fill="var(--red)"/>
  </svg>
  <svg class="deco" style="left:955px;top:760px" width="245" height="600" viewBox="0 0 245 600" aria-hidden="true">
    <path d="M245 0 V600 L22 290 Q-10 240 30 190 Z" fill="var(--navy)"/>
  </svg>
  <svg class="deco" style="left:970px;top:2035px" width="230" height="605" viewBox="0 0 230 605" aria-hidden="true">
    <path d="M230 0 V605 L18 240 Q-5 200 30 160 Z" fill="var(--red)"/>
  </svg>
  <div class="deco photo" role="img" aria-label="Hand zeichnet Wireframes auf ein Whiteboard" style="left:40px;top:2240px;width:280px;height:680px;clip-path:polygon(0 0,60% 22%,100% 50%,85% 62%,0 100%);background:linear-gradient(135deg,#e5e8ec,#b9a39a)"></div>
  <div class="deco photo" role="img" aria-label="Lächelnder Mitarbeiter am Schreibtisch" style="left:1000px;top:3620px;width:200px;height:547px;clip-path:polygon(100% 0,100% 100%,60% 100%,0 40%,55% 5%);background:linear-gradient(160deg,#e9e5df,#b8a99a)"></div>

  <section>
    <h2 class="abs section-title" style="left:340px;top:12px;width:520px">Abrechnung auf Erfolgsbasis –<br>garantiert!</h2>
    <p class="abs center" style="left:296px;top:104px;width:606px">Wie jetzt? Erst bezahlen, wenn die Optimierung erfolgreich war? Genauso ist es! Als erfahrene SEO Agentur bietet wir unsere Leistungen als eine der wenigen zu 100 Prozent auf Erfolgsbasis an. Das heißt, dass Sie von uns erst dann eine Rechnung erhalten, wenn Ihre Webseite auf der 1. Seite der Suchergebnisse rankt. Durch die präzise Zielvorgabe ist sichergestellt, dass Sie keinerlei Risiko eingehen und wir wie immer unser Bestes geben. Warum wir das machen? Weil wir über Jahre hinweg die perfekte Strategie für ein besseres Ranking erforscht haben und damit bisher noch jeden Kunden nach vorne gebracht haben.</p>
    <a class="abs btn" href="#beratung" style="left:415px;top:294px;width:371px">Jetzt unverbindliche Beratung vereinbaren</a>
  </section>

  <section>
    <div class="abs side" style="left:137px;top:468px;width:296px">
      <div class="side-title">Was ist SEO?</div>
      <p>SEO steht für Search Engine Optimization, zu Deutsch Suchmaschinenoptimierung, und ist eine der wichtigsten Disziplinen im Online Marketing. Wer heute Informationen benötigt oder ein Problem lösen will, der konsultiert eine Suchmaschine – allen voran Findora. Doch eins wissen Sie selbst am besten: Kaum jemand schaut sich die Suchergebnisse außerhalb von Seite eins an. Umso wichtiger ist es, mit seiner Webseite genau hier zu ranken. Das aber wollen viele, deshalb führt für erfolgreiche Webseiten kein Weg an der Suchmaschinenoptimierung vorbei. Wir als SEO Agentur unterstützen Sie dabei, aus den zahlreichen Elementen, die für die Suchmaschinenoptimierung notwendig sind, eine funktionierende Verbindung zu schaffen.</p>
    </div>
    <div class="abs" role="img" aria-label="Dezente Linienillustration mit Laborgeräten und Diagrammen" style="left:460px;top:388px;width:330px;height:364px;border-radius:50%;background:radial-gradient(circle,#ececef 0%,rgba(236,236,239,0) 70%)"></div>
    <div class="abs side" style="left:810px;top:468px;width:252px;text-align:right">
      <div class="side-title">Was bringt SEO?</div>
      <p>Eine prominente Position in den Suchergebnissen führt zu einer Kettenreaktion, die sich jeder Unternehmer wünscht. Je besser Sichtbarkeit und Reichweite, desto mehr Traffic spült Findora auf Ihre Webseite. Wir als führende SEO Agentur sorgen dafür, dass es sich dabei um qualifizierten Traffic handelt, aus dem auch zahlende Kunden werden. Dadurch steigt nicht nur Ihre Konversionsrate, sondern natürlich auch der Umsatz Ihres Unternehmens. Suchmaschinenoptimierung macht sich also bezahlt!</p>
    </div>
  </section>

  <section>
    <h2 class="abs" style="left:137px;top:928px;font-size:29px;text-align:left">Warum wir?</h2>
    <div class="abs" style="left:137px;top:972px;font-size:19px;font-weight:300;color:#a5a5aa">SEO Agentur mit Herz, Verstand und ganz viel Erfahrung</div>
    <p class="abs" style="left:137px;top:1020px;width:700px">Seit über zehn Jahren forschen wir schwerpunktmäßig an der perfekten Zusammensetzung effektiver Suchmaschinenoptimierung. Als reine SEO Agentur haben wir uns ganz bewusst dafür entschieden, nicht die gesamte Palette des Online Marketings anzubieten, sondern das, wofür unser Herz schlägt und das, was den größten und vor allem nachhaltigsten Erfolg verspricht. Seitdem ist SEO mehr als unser Forschungsgebiet. SEO ist unsere Leidenschaft. Und genau die Liebe zu dem, was wir tun, macht uns so gut, dass wir ausschließlich auf Erfolgsbasis arbeiten.</p>

    <article class="abs card" style="left:137px;top:1237px;width:292px;height:421px">
      <div class="photo" role="img" aria-label="Berater im Anzug mit Unterlagen im Büro"></div>
      <h3>SEO für Anwälte und Steuerberater</h3>
      <p>Große Rechtsanwalts- und Steuerberaterkanzleien dominieren den Markt. Mit SEO können sich auch kleine und regionale Anwälte, Notare, Steuer- und Unternehmensberater durchsetzen. Wir helfen Ihnen, sich online als Experte zu profilieren.</p>
    </article>
    <article class="abs card" style="left:454px;top:1237px;width:292px;height:421px">
      <div class="photo" role="img" aria-label="Arzt im Gespräch mit einer Patientin"></div>
      <h3>SEO für Ärzte und Apotheker</h3>
      <p>Ärzte und Apotheker können mit einer suchmaschinen-optimierten Webseite nicht nur neue Patienten und Kunden gewinnen, sondern diesen auch langfristig binden und ihnen zeitgemäße Serviceleistungen anbieten.</p>
    </article>
    <article class="abs card" style="left:771px;top:1237px;width:291px;height:421px">
      <div class="photo" role="img" aria-label="Übergabe eines Versandkartons"></div>
      <h3>SEO für (Online-)Händler</h3>
      <p>Der Online-Handel boomt, entsprechend groß ist auch die Konkurrenz. Ein Online-Shop ist noch lange kein Selbstläufer und bedarf besonderen Know-hows bei der Suchmaschinen-optimierung. Wir steigern Ihre Verkaufszahlen nachhaltig!</p>
    </article>

    <article class="abs card" style="left:137px;top:1690px;width:292px;height:432px">
      <div class="photo" role="img" aria-label="Handwerker mit Werkzeuggürtel in der Werkstatt"></div>
      <h3>SEO für Handwerker und<br>Dienstleister</h3>
      <p>Wer einen Handwerker oder Dienstleister sucht, der schaut nicht mehr ins Branchenbuch Orbis, sondern sucht online. Ohne sichtbare Webseite sind Sie für den Kunden quasi nicht existent. Mit Local SEO lässt sich das bereits mit einfachen Mitteln und für kleines Geld ändern!</p>
    </article>
    <article class="abs card" style="left:454px;top:1690px;width:292px;height:432px">
      <div class="photo" role="img" aria-label="Hand zeichnet Website-Entwürfe auf Glaswand"></div>
      <h3>SEO für Online-Portale</h3>
      <p>Online-Portale sind von den Suchmaschinen so abhängig wie kaum ein anderes Internetangebot. Nur wer bei Findora ganz oben steht, erhält ausreichend Traffic um zu überleben. Wir sichern die Zukunft Ihres Portals und bringen Sie in die schwarzen Zahlen.</p>
    </article>
    <article class="abs card" style="left:771px;top:1690px;width:291px;height:432px">
      <div class="photo" role="img" aria-label="Team arbeitet gemeinsam am Computer"></div>
      <h3>SEO für Sie</h3>
      <p>Es gibt keine Branche, die heutzutage ohne Suchmaschinenoptimierung auskommt. Mit zielgerichteten Maßnahmen setzen wir auch Ihr Business auf ein neues Level, ganz egal wie groß Ihr Unternehmen ist. Sprechen Sie uns noch heute an!</p>
    </article>
  </section>

  <section id="beratung">
    <svg class="abs" style="left:572px;top:2218px" width="56" height="56" viewBox="0 0 56 56" aria-hidden="true" fill="none" stroke="var(--red)" stroke-width="2">
      <polygon points="28,16 38,22 38,34 28,40 18,34 18,22"/>
      <line x1="28" y1="16" x2="28" y2="4"/><line x1="28" y1="40" x2="28" y2="52"/>
      <line x1="38" y1="22" x2="48" y2="16"/><line x1="18" y1="22" x2="8" y2="16"/>
      <line x1="38" y1="34" x2="48" y2="40"/><line x1="18" y1="34" x2="8" y2="40"/>
      <circle cx="28" cy="28" r="4"/>
    </svg>
    <h2 class="abs section-title" style="left:300px;top:2300px;width:600px;font-size:29px">Lassen Sie sich beraten.<br>Kostenlos und unverbindlich.</h2>
    <p class="abs center" style="left:296px;top:2400px;width:606px">Seit über zehn Jahren forschen wir schwerpunktmäßig an der perfekten Zusammensetzung effektiver Suchmaschinenoptimierung. Als reine SEO Agentur haben wir uns ganz bewusst dafür entschieden, nicht die gesamte Palette des Online Marketings anzubieten, sondern das, wofür unser Herz schlägt und das, was den größten und vor allem nachhaltigsten Erfolg verspricht. Seitdem ist SEO mehr als unser Forschungsgebiet. SEO ist unsere Leidenschaft. Und genau die Liebe zu dem, was wir tun, macht uns so gut, dass wir ausschließlich auf Erfolgsbasis arbeiten.</p>
    <a class="abs btn" href="#beratung" style="left:429px;top:2571px;width:342px">Jetzt unverbindliche Beratung vereinbaren</a>
  </section>

  <section>
    <h2 class="abs" style="left:250px;top:2778px;width:700px;font-size:30px;line-height:44px">Wir stellen die richtige Verbindung her<br>Schritt für Schritt zur erfolgreichen Webseite</h2>
    <svg class="abs" style="left:216px;top:3002px" width="40" height="40" viewBox="0 0 40 40" aria-label="Zurück" fill="none" stroke="var(--navy)" stroke-width="2">
      <circle cx="20" cy="20" r="17"/><path d="M28 20H12M18 14l-6 6 6 6"/>
    </svg>
    <svg class="abs" style="left:944px;top:3002px" width="40" height="40" viewBox="0 0 40 40" aria-label="Weiter" fill="none" stroke="var(--navy)" stroke-width="2">
      <circle cx="20" cy="20" r="17"/><path d="M12 20h16M22 14l6 6-6 6"/>
    </svg>
    <svg class="abs" style="left:295px;top:2950px" width="130" height="146" viewBox="0 0 130 146" aria-hidden="true">
      <polygon points="65,4 124,38 124,108 65,142 6,108 6,38" fill="#e9ebef"/>
      <polygon points="65,16 113,44 113,102 65,130 17,102 17,44" fill="var(--white)"/>
      <text x="22" y="58" font-family="Lato,sans-serif" font-size="13" fill="var(--navy)">1</text>
      <text x="65" y="88" text-anchor="middle" font-family="Lato,sans-serif" font-size="40" font-weight="400" fill="var(--navy)">AL</text>
    </svg>
    <div class="abs" style="left:454px;top:2908px;font-size:18px;color:#333;font-weight:400">1. Analyse</div>
    <p class="abs" style="left:454px;top:2940px;width:450px">Bevor wir mit der eigentlichen Optimierung beginnen, nehmen wir uns zunächst die Zeit, um uns ein ausgiebiges Bild vom Ist-Zustand zu verschaffen. Dabei prüfen wir unter anderem mithilfe professioneller SEO-Tools, wie gut Ranking und Sichtbarkeit der vorhandenen Webseite sind, um anschließend gezielte Maßnahmen planen und ergreifen zu können. Wir besprechen gemeinsam mit Ihnen die Analyseergebnisse, erfragen Ihre Vorstellungen sowie Ihre Ziele und beraten Sie kostenlos und unverbindlich zu allen Fragen der Suchmaschinenoptimierung.</p>
  </section>

  <section>
    <h2 class="abs section-title" style="left:250px;top:3220px;width:700px;font-size:29px">Jedes Element trägt zu Ihrem Erfolg bei</h2>
    <article class="abs card feature" style="left:137px;top:3312px;width:292px;height:265px">
      <h3>Mobile SEO</h3>
      <p style="font-size:12px;line-height:20px;margin:0 25px">Je nach Branche erfolgt der Großteil der Seitenaufrufe längst über Smartphones und Tablets. Findora hat deshalb die Mobile-First-Strategie ausgerufen. Nur wer eine für mobile Endgeräte optimierte Webseite hat, kann Spitzenpositionen in den Suchergebnissen belegen. Wir machen Ihre Webseite fit fürs mobile Zeitalter!</p>
    </article>
    <article class="abs card feature" style="left:454px;top:3312px;width:292px;height:265px">
      <h3>Local SEO</h3>
      <p style="font-size:12px;line-height:20px;margin:0 25px">50 Prozent der Suchanfragen, die über eine Smartphone getätigt werden, sind lokal. Mit Local SEO beherrschen Sie auch den lokalen Suchindex und können sich über Kunden aus der Umgebung und mit einer deutlich höheren Kaufabsicht freuen – selbst ohne eigene Webseite. Wir zeigen Ihnen, wie das geht!</p>
    </article>
    <article class="abs card feature" style="left:771px;top:3312px;width:291px;height:265px">
      <h3>Image SEO</h3>
      <p style="font-size:12px;line-height:20px;margin:0 25px">Multimedialer Content spricht die Besucher nicht nur besser an, er gefällt auch Findora. Insbesondere Bilder lassen sich gezielt optimieren, um auch über die Findora Bildersuche Traffic zu generieren. Dabei kommt es vor allem darauf an, der Suchmaschine dabei zu helfen, das Motiv zu interpretieren. Wir erschließen gern neue Trafficquellen für Sie!</p>
    </article>
  </section>

  <section>
    <h2 class="abs section-title" style="left:300px;top:3678px;width:600px;font-size:29px">Ihre Vorteile auf einen Blick:</h2>
    <div class="benefit" style="left:137px;top:3768px">
      <svg class="tick" viewBox="0 0 30 30" fill="none" stroke="var(--red)" stroke-width="1.6"><circle cx="15" cy="15" r="13"/><path d="M9 15l4 4 8-8"/></svg>
      <div><strong>mehr Traffic, mehr Kunden, mehr Umsatz</strong><span>durch höhere Sichtbarkeit und größere Reichweite</span></div>
    </div>
    <div class="benefit" style="left:137px;top:3835px">
      <svg class="tick" viewBox="0 0 30 30" fill="none" stroke="var(--red)" stroke-width="1.6"><circle cx="15" cy="15" r="13"/><path d="M9 15l4 4 8-8"/></svg>
      <div><strong>Fokus auf erfolgreiches SEO</strong><span>statt alles anzubieten, aber nichts richtig</span></div>
    </div>
    <div class="benefit" style="left:137px;top:3902px">
      <svg class="tick" viewBox="0 0 30 30" fill="none" stroke="var(--red)" stroke-width="1.6"><circle cx="15" cy="15" r="13"/><path d="M9 15l4 4 8-8"/></svg>
      <div><strong>über 10 Jahre SEO-Erfahrung</strong><span>mit eigenen Webseiten und Projekten von Kunden</span></div>
    </div>
    <div class="benefit" style="left:612px;top:3768px">
      <svg class="tick" viewBox="0 0 30 30" fill="none" stroke="var(--red)" stroke-width="1.6"><circle cx="15" cy="15" r="13"/><path d="M9 15l4 4 8-8"/></svg>
      <div><strong>100 % erfolgsbasiert</strong><span>erst bezahlen, wenn Sie auf Seite 1 sind</span></div>
    </div>
    <div class="benefit" style="left:612px;top:3835px">
      <svg class="tick" viewBox="0 0 30 30" fill="none" stroke="var(--red)" stroke-width="1.6"><circle cx="15" cy="15" r="13"/><path d="M9 15l4 4 8-8"/></svg>
      <div><strong>kostenlose Beratung</strong><span>und unverbindliche Angebotserstellung</span></div>
    </div>
  </section>

  <section>
    <h2 class="abs" style="left:300px;top:4054px;width:600px;font-size:29px;line-height:37px">Fordern Sie jetzt eine kostenlose und<br>unverbindliche Beratung an</h2>
  </section>

</main>
</body>
</html>
```